Morvela Aesthetic Doctor

I require an elegant, luxurious looking business card for my aesthetic business. I am a doctor and that will set me aside from competitors. I am planning to provide home and spa based treatments to clients with high expectations. I have attached my logo.

```html
<!DOCTYPE html>
<html lang="en">
<head>
<meta charset="utf-8">
<title>Morvela Aesthetic Doctor – Business Card</title>
<link rel="stylesheet" href="https://fonts.googleapis.com/css2?family=Cormorant+Garamond:wght@400;600&family=Roboto+Condensed:wght@300&family=Montserrat:wght@300;500&display=swap">
<style>
  :root {
    --backdrop: #d6d6d6;
    --card: #ffffff;
    --brand-blue: #00aeef;
    --mark-blue: #5bc3ee;
    --mark-light: #b9e4f7;
    --stone: #a4a7aa;
    --text-grey: #8d9094;
    --ink: #333333;
  }
  * { margin: 0; padding: 0; box-sizing: border-box; }
  html, body { width: 1200px; height: 800px; overflow: hidden; }
  body { background: var(--backdrop); position: relative; font-family: "Roboto Condensed", sans-serif; }

  .card {
    position: absolute; top: 250px; width: 540px; height: 300px;
    background: var(--card); overflow: hidden;
  }
  .card--front { left: 30px; }
  .card--back { left: 630px; }
  .card__art { position: absolute; inset: 0; }

  .wordmark { position: absolute; font-family: "Cormorant Garamond", serif; font-weight: 400; color: var(--stone); line-height: 1; }
  .wordmark__name { display: block; letter-spacing: 1px; }
  .wordmark__line { display: block; }

  .card--front .wordmark { left: 17px; top: 16px; }
  .card--front .wordmark__name { font-size: 38px; }
  .card--front .wordmark__line { font-size: 17px; letter-spacing: 1.2px; margin-top: 2px; }

  .doctor { position: absolute; left: 17px; top: 104px; display: flex; align-items: baseline; }
  .doctor__name { font-family: "Cormorant Garamond", serif; font-weight: 600; font-size: 25px; color: var(--brand-blue); }
  .doctor__post { font-family: "Roboto Condensed", sans-serif; font-weight: 300; font-size: 12px; color: var(--text-grey); border-left: 1.5px solid var(--ink); padding-left: 6px; margin-left: 8px; line-height: 18px; }
  .doctor__diploma { position: absolute; left: 17px; top: 134px; font-weight: 300; font-size: 13px; color: var(--text-grey); }

  .contact { position: absolute; left: 17px; top: 168px; list-style: none; font-family: "Montserrat", sans-serif; font-weight: 300; font-size: 12.5px; color: var(--text-grey); }
  .contact li { display: flex; align-items: center; height: 17px; }
  .contact svg { width: 12px; height: 12px; margin-right: 8px; stroke: var(--brand-blue); fill: none; stroke-width: 1.5; }
  .contact strong { font-weight: 500; color: var(--brand-blue); }
  .social { display: inline-flex; gap: 10px; margin-left: 30px; }
  .social span { width: 13px; height: 13px; border-radius: 50%; background: var(--brand-blue); }

  .services { position: absolute; left: 17px; top: 237px; font-weight: 300; font-size: 13px; line-height: 17px; color: var(--text-grey); }

  .card--back .wordmark { left: 232px; top: 108px; }
  .card--back .wordmark__name { font-size: 64px; letter-spacing: 2px; }
  .card--back .wordmark__line { font-size: 27px; letter-spacing: 1.5px; margin-top: 2px; }
  .tagline { position: absolute; left: 0; right: 0; top: 271px; padding-left: 32px; text-align: center; font-family: "Cormorant Garamond", serif; font-weight: 600; font-size: 13.5px; letter-spacing: 0.6px; color: var(--brand-blue); }
</style>
</head>
<body>

<section class="card card--front" aria-label="Business card front">
  <svg class="card__art" viewBox="0 0 540 300" aria-hidden="true">
    <circle cx="450" cy="145" r="147" fill="none" stroke="var(--brand-blue)" stroke-width="5"/>
    <circle cx="450" cy="145" r="143" fill="var(--stone)"/>
    <rect x="0" y="0" width="1" height="1" fill="none"/>
  </svg>
  <svg class="card__art" viewBox="0 0 540 300">
    <circle cx="440" cy="143" r="76" fill="url(#markFront)" stroke="var(--card)" stroke-width="4" role="img" aria-label="Brand symbol area"/>
    <defs>
      <radialGradient id="markFront" cx="0.45" cy="0.45" r="0.6">
        <stop offset="0" stop-color="var(--mark-light)"/>
        <stop offset="1" stop-color="var(--mark-blue)"/>
      </radialGradient>
    </defs>
  </svg>

  <div class="wordmark">
    <span class="wordmark__name">MORVELA</span>
    <span class="wordmark__line">AESTHETIC DOCTOR</span>
  </div>

  <div class="doctor">
    <span class="doctor__name">Dr Elise Varner</span>
    <span class="doctor__post">MRCPCH MD</span>
  </div>
  <p class="doctor__diploma">Australasian Diploma of Aesthetic Medicine</p>

  <ul class="contact">
    <li><svg viewBox="0 0 12 12"><path d="M2 1.5 L4 1.5 L5 4 L3.8 5 Q5 7.5 7 8.2 L8 7 L10.5 8 L10.5 10 Q5 10.5 2 5 Z"/></svg>0800 555 014</li>
    <li><svg viewBox="0 0 12 12"><rect x="1" y="2.5" width="10" height="7"/><path d="M1 2.5 L6 6.5 L11 2.5"/></svg>elise@morvela.co.nz</li>
    <li><svg viewBox="0 0 12 12"><circle cx="6" cy="6" r="5"/><path d="M1 6 H11 M6 1 Q3 6 6 11 M6 1 Q9 6 6 11"/></svg>www.<strong>morvela</strong>.co.nz
      <span class="social" aria-label="Social media"><span></span><span></span></span></li>
  </ul>

  <p class="services">Dermal injectables - Plasma facials - Microneedling<br>Skin boosters - Excessive sweating<br>Home and Spa Based Treatments</p>
</section>

<section class="card card--back" aria-label="Business card back">
  <svg class="card__art" viewBox="0 0 540 300">
    <path d="M0 2 Q18 2 34 5" fill="none" stroke="var(--brand-blue)" stroke-width="2.5"/>
    <path d="M0 296 Q70 290 110 243" fill="none" stroke="var(--brand-blue)" stroke-width="5"/>
    <defs>
      <radialGradient id="markBack" cx="0.45" cy="0.45" r="0.6">
        <stop offset="0" stop-color="var(--mark-light)"/>
        <stop offset="1" stop-color="var(--mark-blue)"/>
      </radialGradient>
    </defs>
    <circle cx="172" cy="150" r="48" fill="url(#markBack)" stroke="var(--stone)" stroke-width="2.5" role="img" aria-label="Brand symbol area"/>
  </svg>

  <div class="wordmark">
    <span class="wordmark__name">MORVELA</span>
    <span class="wordmark__line">AESTHETIC DOCTOR</span>
  </div>

  <p class="tagline">HOME AND SPA BASED TREATMENTS</p>
</section>

</body>
</html>
```